Newspaper AD in the Restaurant Section HOMECARE/Senior Living

Looking for an ad that is 6.425 inches wide and 5 inches tall to go into the newspaper weekly it will be in the restaurant section. We are a senior homecare company and we are looking to show clients that caregivers are able to assist them not only in personal care needs but also meal prep. We would like the design to have the feel of our existing ad or our newly launched website. It will be in the Savor section of the Kailani Courier which is not where we normally would advertise as a homecare agency so ad has to have some kind of feel for that section.
It should say somewhere maybe by contact info Call today for FREE Consultation.

Target Market(s)

Target market is Men/Women ages 35-105

Industry/Entity Type

Homecare and Senior Living

Font styles to use
Sans Serif

Colors
0054AA
0677BA
7BADD7
CADEEF
E8F1F8
FFF300
FFF600
FEFA6F
FFFEC7
FFFEE8
EB3D1F
EC4F4E
F09395
F8D3D4
FCEDEE

Requirements
Must have
• Logo, Contact info: Phone number (808) 555-0173, email address Info@brightmorehome.com and website www.Brightmorehome.com.
Nice to have
• Something that will be eye catching and to the point. Maybe a picture of a caregiver preparing a meal with an elderly person

```html
<!DOCTYPE html>
<html lang="en">
<head>
<meta charset="utf-8">
<title>Brightmore Homecare – Newspaper Ad</title>
<link rel="stylesheet" href="https://fonts.googleapis.com/css2?family=Montserrat:wght@500;600;700&display=swap">
<style>
  :root {
    --page-bg: #f29690;
    --blue: #0677ba;
    --coral: #f3937e;
    --coral-soft: #f09395;
    --green: #0e6b5c;
    --white: #ffffff;
  }
  html, body {
    margin: 0;
    padding: 0;
    width: 682px;
    height: 1200px;
    overflow: hidden;
    background: var(--page-bg);
    font-family: "Montserrat", sans-serif;
  }
  .ad {
    position: absolute;
    left: 21px;
    top: 351px;
    width: 640px;
    height: 498px;
    background: var(--white);
    overflow: hidden;
    box-shadow: 0 6px 14px rgba(0,0,0,0.18);
  }
  .ad-art {
    position: absolute;
    inset: 0;
  }
  .brand {
    position: absolute;
    left: 32px;
    top: 20px;
    width: 210px;
    text-align: center;
    color: var(--green);
    font-weight: 700;
  }
  .brand-mark {
    width: 60px;
    height: 60px;
    margin: 0 auto 14px;
    background: var(--coral);
    border-radius: 10px;
  }
  .brand-name {
    font-size: 31px;
    line-height: 1;
    letter-spacing: -0.5px;
  }
  .brand-tagline {
    margin-top: 6px;
    font-size: 13px;
    letter-spacing: 8px;
  }
  .headline {
    position: absolute;
    left: 24px;
    top: 236px;
    margin: 0;
    color: var(--white);
    font-size: 20.5px;
    line-height: 25.5px;
    font-weight: 700;
  }
  .services-label {
    position: absolute;
    left: 24px;
    top: 352px;
    width: 221px;
    height: 28px;
    background: var(--coral);
    color: var(--white);
    font-size: 18.5px;
    font-weight: 700;
    line-height: 28px;
    text-align: center;
  }
  .service-list {
    position: absolute;
    left: 26px;
    top: 389px;
    margin: 0;
    padding: 0;
    list-style: none;
    color: var(--white);
    font-size: 12.3px;
    font-weight: 500;
    line-height: 14.5px;
  }
  .service-list li {
    position: absolute;
    top: 0;
    padding-left: 16px;
    white-space: nowrap;
  }
  .service-list svg {
    position: absolute;
    left: 0;
    top: 3px;
    width: 13px;
    height: 13px;
  }
  .call-pill {
    position: absolute;
    left: 19px;
    top: 428px;
    width: 250px;
    height: 34px;
    border: 1.5px solid var(--coral);
    border-radius: 10px;
    overflow: hidden;
    display: flex;
    align-items: center;
  }
  .call-label {
    width: 98px;
    height: 100%;
    background: var(--coral);
    color: var(--white);
    font-size: 15px;
    font-weight: 700;
    display: flex;
    align-items: center;
    padding-left: 7px;
    box-sizing: border-box;
    white-space: nowrap;
  }
  .call-icon {
    width: 15px;
    height: 15px;
    margin-left: -20px;
    margin-right: 12px;
    flex: none;
  }
  .call-number {
    color: var(--white);
    font-size: 16px;
    font-weight: 600;
    white-space: nowrap;
  }
  .consultation {
    position: absolute;
    left: 24px;
    top: 472px;
    margin: 0;
    color: var(--white);
    font-size: 12px;
    font-weight: 600;
    white-space: nowrap;
  }
  .consultation strong {
    font-weight: 600;
  }
  .contact-row {
    position: absolute;
    left: 282px;
    right: 12px;
    top: 437px;
    display: flex;
    justify-content: space-between;
    align-items: center;
    color: var(--white);
    font-size: 10.5px;
    font-weight: 500;
  }
  .contact {
    display: flex;
    align-items: center;
    gap: 4px;
    white-space: nowrap;
  }
  .contact svg { width: 15px; height: 15px; flex: none; }
</style>
</head>
<body>
<div class="ad">
  <svg class="ad-art" viewBox="0 0 640 498" width="640" height="498">
    <defs>
      <linearGradient id="photoTone" x1="0" y1="0" x2="1" y2="1">
        <stop offset="0" stop-color="#7a3a26"/>
        <stop offset="0.45" stop-color="#b98a6a"/>
        <stop offset="1" stop-color="#d8d4b8"/>
      </linearGradient>
      <linearGradient id="circleOneTone" x1="0" y1="0" x2="1" y2="1">
        <stop offset="0" stop-color="#c9b48a"/>
        <stop offset="1" stop-color="#3d7fc4"/>
      </linearGradient>
      <linearGradient id="circleTwoTone" x1="0" y1="0" x2="1" y2="1">
        <stop offset="0" stop-color="#9bb87e"/>
        <stop offset="1" stop-color="#c8dcea"/>
      </linearGradient>
      <linearGradient id="rimTone" x1="0" y1="0" x2="0" y2="1">
        <stop offset="0" stop-color="#f09395"/>
        <stop offset="1" stop-color="#7badd7"/>
      </linearGradient>
    </defs>

    <g role="img" aria-label="Photo: a caregiver serving a fresh meal to an older couple at their dining table">
      <path d="M340 0 H640 V340 H330 C280 290 255 220 262 150 C268 90 295 40 340 0 Z" fill="url(#photoTone)"/>
    </g>
    <path d="M340 0 C295 40 268 90 262 150 C255 220 280 290 330 340" fill="none" stroke="url(#rimTone)" stroke-width="4"/>

    <path d="M0 186 C110 168 230 186 330 232 L440 296 L640 322 V498 H0 Z" fill="var(--coral-soft)"/>
    <path d="M0 192 C110 176 230 194 330 244 L440 306 L640 330 V498 H0 Z" fill="var(--blue)"/>

    <g role="img" aria-label="Photo: a caregiver and a smiling client sharing a drink on the sofa">
      <circle cx="394" cy="279" r="69" fill="url(#circleOneTone)" stroke="url(#rimTone)" stroke-width="4"/>
    </g>
    <g role="img" aria-label="Photo: an older woman enjoying a healthy plated meal">
      <circle cx="521" cy="306" r="69" fill="url(#circleTwoTone)" stroke="url(#rimTone)" stroke-width="4"/>
    </g>
  </svg>

  <div class="brand">
    <div class="brand-mark"></div>
    <div class="brand-name">Brightmore</div>
    <div class="brand-tagline">HOMECARE</div>
  </div>

  <p class="headline">Personal care services<br>to meet your loved ones<br>needs in the comfort and<br>safety of their own home.</p>

  <div class="services-label">Homecare Services</div>

  <ul class="service-list">
    <li style="left:0"><svg viewBox="0 0 14 14"><rect x="1" y="2" width="11" height="11" fill="none" stroke="#f3937e" stroke-width="1.4"/><path d="M3.5 7 L6 9.8 L13 1" fill="none" stroke="#f3937e" stroke-width="1.6"/></svg>Home<br>Health Aides</li>
    <li style="left:101px"><svg viewBox="0 0 14 14"><rect x="1" y="2" width="11" height="11" fill="none" stroke="#f3937e" stroke-width="1.4"/><path d="M3.5 7 L6 9.8 L13 1" fill="none" stroke="#f3937e" stroke-width="1.6"/></svg>Skilled<br>Nursing (RN/LPN)</li>
    <li style="left:231px"><svg viewBox="0 0 14 14"><rect x="1" y="2" width="11" height="11" fill="none" stroke="#f3937e" stroke-width="1.4"/><path d="M3.5 7 L6 9.8 L13 1" fill="none" stroke="#f3937e" stroke-width="1.6"/></svg>Bathing &amp;<br>Meal Service</li>
    <li style="left:331px"><svg viewBox="0 0 14 14"><rect x="1" y="2" width="11" height="11" fill="none" stroke="#f3937e" stroke-width="1.4"/><path d="M3.5 7 L6 9.8 L13 1" fill="none" stroke="#f3937e" stroke-width="1.6"/></svg>Medication<br>Management</li>
    <li style="left:448px"><svg viewBox="0 0 14 14"><rect x="1" y="2" width="11" height="11" fill="none" stroke="#f3937e" stroke-width="1.4"/><path d="M3.5 7 L6 9.8 L13 1" fill="none" stroke="#f3937e" stroke-width="1.6"/></svg>Services<br>Available 24/7</li>
  </ul>

  <div class="call-pill">
    <div class="call-label">Call Now</div>
    <svg class="call-icon" viewBox="0 0 16 16"><rect width="16" height="16" fill="#ffffff"/><path d="M5 3.5 L7 3.5 L7.6 6 L6.4 7 C7 8.4 7.8 9.3 9.1 9.8 L10.1 8.6 L12.5 9.2 L12.5 11.2 C8 11.5 4.6 8 5 3.5 Z" fill="#0677ba"/></svg>
    <span class="call-number">(808) 555-0173</span>
  </div>

  <p class="consultation">Call today for <strong>FREE</strong> Consultation</p>

  <div class="contact-row">
    <div class="contact contact-email">
      <svg viewBox="0 0 16 16"><rect width="16" height="16" rx="2" fill="#f3937e"/><rect x="3" y="4.5" width="10" height="7" fill="none" stroke="#fff" stroke-width="1.2"/><path d="M3 4.5 L8 8.5 L13 4.5" fill="none" stroke="#fff" stroke-width="1.2"/></svg>
      <span>Info@brightmorehome.com</span>
    </div>
    <div class="contact contact-web">
      <svg viewBox="0 0 16 16"><rect width="16" height="16" rx="2" fill="#f3937e"/><circle cx="8" cy="8" r="5" fill="none" stroke="#fff" stroke-width="1.1"/><ellipse cx="8" cy="8" rx="2.2" ry="5" fill="none" stroke="#fff" stroke-width="1"/><path d="M3 8 H13" stroke="#fff" stroke-width="1"/></svg>
      <span>www.Brightmorehome.com</span>
    </div>
  </div>
</div>
</body>
</html>
```